KVT Building And Maintenance

Need a very professional looking double sided Buisiness card with all my details phone number, name, email, license number.

Target Market(s)

construction industry

Industry/Entity Type

building

Contact Information for Business Card

Name Dale Pemberton. Email Address Info@KVTBuilding.com.au mobile number 0452918736 licence number 671093D. web site

```html
<!DOCTYPE html>
<html lang="en">
<head>
<meta charset="utf-8">
<title>KVT Building And Maintenance – Business Card</title>
<link rel="stylesheet" href="https://fonts.googleapis.com/css2?family=Montserrat:wght@400;500;700;800&display=swap">
<style>
  :root {
    --backdrop: #5a5a5a;
    --card: #262626;
    --accent: #4a9bd8;
    --ink: #ffffff;
    --ink-soft: #e6e6e6;
  }
  * { box-sizing: border-box; margin: 0; padding: 0; }
  html, body {
    width: 1200px; height: 900px; overflow: hidden;
    background: var(--backdrop);
    font-family: "Montserrat", sans-serif;
  }
  .sheet {
    width: 1200px; height: 900px;
    display: flex; flex-direction: column;
    align-items: center; justify-content: center; gap: 40px;
  }
  .card {
    position: relative;
    width: 700px; height: 400px;
    background: var(--card);
    border-bottom: 6px solid var(--accent);
    box-shadow: 0 8px 22px rgba(0,0,0,.35);
  }
  .brand {
    display: flex; align-items: center; gap: 14px;
    color: var(--ink);
    font-weight: 800;
    letter-spacing: 2px;
    line-height: 1;
  }
  .brand-mark {
    width: 22px; height: 22px; background: var(--accent);
  }
  .card-front .brand {
    position: absolute; left: 50%; top: 50%;
    transform: translate(-50%, -50%);
    font-size: 54px;
  }
  .card-back .brand {
    position: absolute; right: 48px; top: 70px;
    font-size: 38px;
  }
  .card-back .brand .brand-mark { width: 16px; height: 16px; }
  .holder {
    position: absolute; left: 48px; top: 150px;
  }
  .holder-name {
    color: var(--accent);
    font-weight: 700; font-size: 30px; letter-spacing: 1px;
    text-transform: uppercase;
  }
  .holder-role {
    color: var(--ink-soft);
    font-weight: 400; font-size: 17px; margin-top: 4px; margin-left: 22px;
  }
  .details {
    position: absolute; left: 150px; bottom: 34px;
    color: var(--ink-soft); font-size: 17px; font-weight: 400;
  }
  .licence { margin-bottom: 16px; }
  .contact-list { list-style: none; display: flex; flex-direction: column; gap: 8px; }
  .contact-item { display: flex; align-items: center; gap: 10px; }
  .contact-icon {
    width: 22px; height: 22px; border-radius: 50%;
    background: var(--accent);
    display: flex; align-items: center; justify-content: center;
    flex: none;
  }
</style>
</head>
<body>
<main class="sheet">
  <section class="card card-front">
    <div class="brand"><span class="brand-mark"></span>KVT BUILDING</div>
  </section>

  <section class="card card-back">
    <div class="holder">
      <p class="holder-name">Dale Pemberton</p>
      <p class="holder-role">Managing Director</p>
    </div>

    <div class="brand"><span class="brand-mark"></span>KVT BUILDING</div>

    <div class="details">
      <p class="licence">Licence Number 671093D</p>
      <ul class="contact-list">
        <li class="contact-item">
          <span class="contact-icon">
            <svg width="12" height="12" viewBox="0 0 24 24" fill="#262626"><path d="M6.6 10.8a15.1 15.1 0 0 0 6.6 6.6l2.2-2.2c.3-.3.7-.4 1-.2 1.1.4 2.3.6 3.6.6.6 0 1 .4 1 1V20c0 .6-.4 1-1 1A17 17 0 0 1 3 4c0-.6.4-1 1-1h3.5c.6 0 1 .4 1 1 0 1.3.2 2.5.6 3.6.1.3 0 .7-.2 1z"/></svg>
          </span>
          0452918736
        </li>
        <li class="contact-item">
          <span class="contact-icon">
            <svg width="12" height="12" viewBox="0 0 24 24" fill="none" stroke="#262626" stroke-width="2.5"><rect x="3" y="5" width="18" height="14"/><path d="M3 5l9 8 9-8"/></svg>
          </span>
          Info@KVTBuilding.com.au
        </li>
        <li class="contact-item">
          <span class="contact-icon">
            <svg width="12" height="12" viewBox="0 0 24 24" fill="none" stroke="#262626" stroke-width="2.5"><circle cx="12" cy="12" r="9"/><path d="M3 12h18M12 3c3 3 3 15 0 18M12 3c-3 3-3 15 0 18"/></svg>
          </span>
          www.KVTBuilding.com.au
        </li>
      </ul>
    </div>
  </section>
</main>
</body>
</html>
```